Business Card Design Project

double sided, embossed, name & logo on front font sonsie one, back Name Maribel Stoddart, mobile 0468214093, Phone 76139584,
email maribel@brightwipe.com, use sysbols on the back for example an envelope for email, a telephone for phone number etc.symbol slate grey writing navy blue

Industry/Entity Type

Business

```html
<!DOCTYPE html>
<html lang="en">
<head>
<meta charset="utf-8">
<title>Bright Wipe Business Card</title>
<link rel="stylesheet" href="https://fonts.googleapis.com/css2?family=Open+Sans:wght@400;600&display=swap">
<style>
  :root {
    --backdrop-light: #b4b4b4;
    --backdrop-dark: #8f8f8f;
    --navy-deep: #020b26;
    --navy: #0a2d5c;
    --navy-mid: #114a86;
    --royal: #2a48a8;
    --royal-light: #5a7fd0;
    --sky: #9ec6e8;
    --white: #ffffff;
    --slate: #3f4650;
    --card-w: 500px;
    --card-h: 286px;
  }
  * { box-sizing: border-box; margin: 0; padding: 0; }
  html, body {
    width: 1200px; height: 861px; overflow: hidden;
  }
  body {
    background: radial-gradient(ellipse at 50% 40%, var(--backdrop-light), var(--backdrop-dark));
    font-family: "Open Sans", Arial, sans-serif;
    position: relative;
  }
  .card {
    position: absolute;
    width: var(--card-w);
    height: var(--card-h);
    border-radius: 4px;
    overflow: hidden;
    box-shadow: 0 14px 30px rgba(0,0,0,0.28);
    color: var(--white);
  }
  .card--front {
    left: 70px; top: 288px;
    background: linear-gradient(160deg, var(--navy-mid) 0%, var(--navy) 40%, var(--navy-deep) 100%);
    display: flex; align-items: center; justify-content: center;
  }
  .brand-name {
    font-family: "Open Sans", Arial, sans-serif;
    font-weight: 600;
    color: var(--white);
    letter-spacing: 0.5px;
  }
  .card--front .brand-name { font-size: 52px; }
  .card--back {
    left: 630px; top: 288px;
    background: linear-gradient(170deg, var(--royal) 0%, var(--royal) 50%, var(--royal-light) 100%);
  }
  .back-shape { position: absolute; inset: 0; }
  .card--back .brand-name {
    position: absolute; left: 26px; top: 70px;
    font-size: 40px;
  }
  .holder-name {
    position: absolute; left: 26px; bottom: 30px;
    font-size: 24px; font-weight: 600;
  }
  .contact-list {
    position: absolute; right: 22px; top: 118px;
    list-style: none;
    text-align: right;
    font-size: 13px; line-height: 1.3;
  }
  .contact-item {
    display: flex; align-items: center; justify-content: flex-end;
    gap: 8px; margin-bottom: 5px;
  }
  .contact-icon {
    width: 18px; height: 18px; flex: none;
  }
  .contact-email {
    position: absolute; right: 22px; bottom: 28px;
    font-size: 13px;
  }
</style>
</head>
<body>

  <section class="card card--front" aria-label="Card front">
    <span class="brand-name">Bright Wipe</span>
  </section>

  <section class="card card--back" aria-label="Card back">
    <svg class="back-shape" viewBox="0 0 500 286" preserveAspectRatio="none" aria-hidden="true">
      <defs>
        <linearGradient id="band-gradient" x1="0" y1="0" x2="1" y2="1">
          <stop offset="0" stop-color="#0d3a70"/>
          <stop offset="1" stop-color="#0a2458"/>
        </linearGradient>
      </defs>
      <polygon points="0,0 500,0 500,26 230,152 0,170" fill="url(#band-gradient)"/>
      <polygon points="0,170 230,152 500,26 500,40 234,166 0,180" fill="#ffffff"/>
      <polygon points="0,180 234,166 500,40 500,56 240,180 0,190" fill="#9ec6e8"/>
    </svg>

    <span class="brand-name">Bright Wipe</span>

    <ul class="contact-list">
      <li class="contact-item">
        <span>48 Harbour Street<br>Glenelg 5045</span>
        <svg class="contact-icon" viewBox="0 0 20 20" aria-label="Address">
          <circle cx="10" cy="10" r="10" fill="#3f4650"/>
          <path d="M10 4a3.6 3.6 0 0 0-3.6 3.6c0 2.7 3.6 7.4 3.6 7.4s3.6-4.7 3.6-7.4A3.6 3.6 0 0 0 10 4z" fill="#fff"/>
          <circle cx="10" cy="7.6" r="1.3" fill="#3f4650"/>
        </svg>
      </li>
      <li class="contact-item">
        <span>0468214093</span>
        <svg class="contact-icon" viewBox="0 0 20 20" aria-label="Mobile">
          <circle cx="10" cy="10" r="10" fill="#3f4650"/>
          <rect x="7" y="4" width="6" height="12" rx="1" fill="#fff"/>
          <rect x="8" y="5.5" width="4" height="7" fill="#3f4650"/>
        </svg>
      </li>
      <li class="contact-item">
        <span>76139584</span>
        <svg class="contact-icon" viewBox="0 0 20 20" aria-label="Phone">
          <circle cx="10" cy="10" r="10" fill="#3f4650"/>
          <path d="M6.5 5l2 .2.8 2.4-1.2 1a6 6 0 0 0 3.3 3.3l1-1.2 2.4.8.2 2A1.5 1.5 0 0 1 13.5 15 8.5 8.5 0 0 1 5 6.5 1.5 1.5 0 0 1 6.5 5z" fill="#fff"/>
        </svg>
      </li>
      <li class="contact-item">
        <span>brightwipe.com</span>
        <svg class="contact-icon" viewBox="0 0 20 20" aria-label="Email">
          <circle cx="10" cy="10" r="10" fill="#3f4650"/>
          <rect x="5" y="6.5" width="10" height="7" fill="#fff"/>
          <path d="M5 6.5l5 4 5-4" fill="none" stroke="#3f4650" stroke-width="1"/>
        </svg>
      </li>
    </ul>

    <span class="holder-name">Maribel Stoddart</span>
    <span class="contact-email">maribel@brightwipe.com</span>
  </section>

</body>
</html>
```